Body corporate management needs business principle flyer design

We need a one page A4 flyer design for our business principles.
We manage body corporates and strata properties.
Brightwick is a new initiative for our company. Its a label that we have given to our principles of business that drive our people, systems and processes to give assurance to our clients that every detail matters.
We would like to be able to include this design in future brochure so we are after 1 x portrait and 1 x landscape.
The design needs to portray professionalism.
We would like to see designs that use the colour red. (see attached logo).

Target Market(s)

Professionals

Industry/Entity Type

Business

Font styles to use
Sans Serif

Requirements
Must have
• Brightwick logo, provide the design file and as pdf
Nice to have
• the use of the colour red from the logo

```html
<!DOCTYPE html>
<html lang="en">
<head>
<meta charset="utf-8">
<title>Brightwick – Principles of Business</title>
<link href="https://fonts.googleapis.com/css2?family=Open+Sans:wght@300;400;600;700&family=Arimo:wght@400&display=swap" rel="stylesheet">
<style>
  :root {
    --red: #e63b2e;
    --ink: #2f2f2f;
    --hero-light: #f4f4f4;
    --hero-mid: #e3e3e3;
    --suit: #1e2a3f;
    --white: #ffffff;
  }
  * { box-sizing: border-box; margin: 0; padding: 0; }
  html, body { width: 857px; height: 1200px; overflow: hidden; background: var(--white); }
  .flyer {
    position: relative;
    width: 857px;
    height: 1200px;
    background: var(--white);
    font-family: "Open Sans", Arial, sans-serif;
    color: var(--ink);
    overflow: hidden;
  }
  .hero {
    position: absolute; left: 0; top: 0;
    width: 857px; height: 291px;
    background: linear-gradient(90deg, var(--hero-light) 30%, var(--hero-mid) 100%);
  }
  .hero-photo {
    position: absolute; left: 0; top: 0;
    width: 315px; height: 291px;
    background: linear-gradient(100deg, var(--suit) 0%, #3a4660 45%, #d9c7b8 75%, var(--hero-light) 100%);
  }
  .hero-pointer {
    position: absolute; left: 0; top: 0;
    width: 857px; height: 291px;
    pointer-events: none;
  }
  .brand-mark {
    position: absolute; left: 380px; top: 84px;
    font-weight: 300; font-size: 80px; line-height: 1;
    color: var(--red); letter-spacing: -0.5px;
  }
  .hero-tagline {
    position: absolute; left: 387px; top: 187px;
    width: 358px;
    font-family: "Arimo", Arial, sans-serif;
    font-size: 15.5px; line-height: 21.5px; color: #222;
    hyphens: manual;
  }
  .title-block { position: absolute; left: 75px; top: 318px; color: var(--red); }
  .title-block .name { font-weight: 700; font-size: 32px; line-height: 1; letter-spacing: -0.3px; }
  .title-block .sub { font-weight: 600; font-size: 16.5px; margin-top: 2px; }

  .column { position: absolute; top: 408px; width: 328px; }
  .column.left { left: 74px; }
  .column.right { left: 456px; top: 409px; }

  .principle { margin-bottom: 8px; }
  .principle h3 {
    display: flex; align-items: center; gap: 16px;
    height: 36px; margin-bottom: 10px;
    font-weight: 600; font-size: 16px; color: var(--red);
  }
  .column.right .principle { margin-bottom: 13px; }
  .column.right .principle + .principle h3 { margin-bottom: 15px; }
  .principle h3 svg { width: 40px; height: 36px; flex: none; }
  .principle p {
    font-size: 12.6px; line-height: 17.3px; text-align: justify;
  }
</style>
</head>
<body>
<div class="flyer">
  <header class="hero">
    <div class="hero-photo" role="img" aria-label="Photo of a businessman in a dark suit pointing a finger forward"></div>
    <svg class="hero-pointer" viewBox="0 0 857 291" aria-hidden="true">
      <circle cx="243" cy="60" r="16" fill="none" stroke="var(--red)" stroke-width="1.5"/>
      <circle cx="243" cy="60" r="10" fill="var(--red)"/>
      <line x1="254" y1="66" x2="366" y2="118" stroke="var(--red)" stroke-width="1.2"/>
    </svg>
    <div class="brand-mark">Brightwick</div>
    <p class="hero-tagline">Brightwick Is our principles Of business that drive our people, systems and processes to give assur-<br>ance to our clients that every detail matters.</p>
  </header>

  <div class="title-block">
    <div class="name">Brightwick</div>
    <div class="sub">Principles of Business</div>
  </div>

  <section class="column left">
    <article class="principle">
      <h3><svg viewBox="0 0 40 36"><path d="M4 13h8l16-9v28l-16-9H4z" fill="var(--red)"/><rect x="8" y="23" width="5" height="9" fill="var(--red)"/><rect x="31" y="4" width="3" height="28" fill="var(--red)"/></svg>Client Experience</h3>
      <p>Our promise is to pursue excellence and to continually deliver a solutions based service. We achieve this through active engagement, open channels of communication and a serviced led team with the dedicated resources to listen, engage and implement.</p>
    </article>
    <article class="principle">
      <h3><svg viewBox="0 0 40 36"><path d="M3 12l9-8 8 6 8-6 9 8-17 18z" fill="none" stroke="var(--red)" stroke-width="2.5" stroke-linejoin="round"/><path d="M12 16l8 8 6-6" fill="none" stroke="var(--red)" stroke-width="2.5"/></svg>Loyalty</h3>
      <p>We seek to develop a life-time relationship with our clients, building trust by acting with integrity, honesty and courtesy. We achieve this due to our expert approach to strata management and providing a responsive service to our clients.</p>
    </article>
    <article class="principle">
      <h3><svg viewBox="0 0 40 36"><path d="M6 32l4-12 16-16 8 8-16 16z" fill="var(--red)"/><line x1="6" y1="32" x2="14" y2="24" stroke="#fff" stroke-width="2"/></svg>Education and Guidance</h3>
      <p>We endeavor to always be proactive in client education and guidance. This is achieved by our internal and external communications, comprehensive training programs and cross-departmental collaboration of knowledge sharing.</p>
    </article>
    <article class="principle">
      <h3><svg viewBox="0 0 40 36"><path d="M20 2l17 9H3z" fill="var(--red)"/><rect x="7" y="14" width="4" height="14" fill="var(--red)"/><rect x="18" y="14" width="4" height="14" fill="var(--red)"/><rect x="29" y="14" width="4" height="14" fill="var(--red)"/><rect x="3" y="30" width="34" height="4" fill="var(--red)"/></svg>Compliance &amp; Governance</h3>
      <p>We engage and own a position of ‘every detail matters’. We give due diligence to the relevant state and national legislations with which we, our clients and our stakeholders must comply. We regulate and achieve this through a robust system of internal processes and protocols which structure and confirm our deliverables are in line with regulations.</p>
    </article>
    <article class="principle">
      <h3><svg viewBox="0 0 40 36"><circle cx="14" cy="15" r="9" fill="none" stroke="var(--red)" stroke-width="6" stroke-dasharray="4 3"/><circle cx="14" cy="15" r="6" fill="var(--red)"/><circle cx="14" cy="15" r="2.5" fill="#fff"/><circle cx="31" cy="26" r="5" fill="var(--red)"/><circle cx="31" cy="26" r="1.8" fill="#fff"/></svg>Systems and processes</h3>
      <p>We strive to be the best in our field, by implementing efficiencies without compromising service quality, accuracy or compliance. We continually seek to achieve this by reviewing, updating and adopting continuous improvement strategies, systems and quality processes that deliver outcomes.</p>
    </article>
  </section>

  <section class="column right">
    <article class="principle">
      <h3><svg viewBox="0 0 40 36"><circle cx="17" cy="19" r="13" fill="none" stroke="var(--red)" stroke-width="2.5"/><path d="M10 18l6 6 15-16" fill="none" stroke="var(--red)" stroke-width="3"/></svg>Quality &amp; Commitment</h3>
      <p>We invest in the recruitment and retention of a quality and diverse team of experienced professionals with a strong focus on continual professional development. As committed and skilled individuals, we actively promote the cross-departmental collaboration with one another to deliver a well rounded offering.</p>
    </article>
    <article class="principle">
      <h3><svg viewBox="0 0 40 36"><path d="M4 3h6l6 26h20" fill="none" stroke="var(--red)" stroke-width="2.5"/><rect x="16" y="8" width="10" height="10" fill="var(--red)"/><rect x="22" y="14" width="12" height="12" fill="var(--red)"/><circle cx="18" cy="32" r="3" fill="none" stroke="var(--red)" stroke-width="2"/></svg>Delivery</h3>
      <p>We empower our teams to deliver an outstanding client service and to be accountable for their actions. We will make sure every detail matters, provide valuable insight and supply information in a clear and timely manner.</p>
    </article>
    <article class="principle">
      <h3><svg viewBox="0 0 40 36"><path d="M9 4h22l7 9-18 20L2 13z" fill="var(--red)"/><path d="M2 13h36M14 4l-3 9 9 20 9-20-3-9" fill="none" stroke="#fff" stroke-width="1.2"/></svg>Integrity</h3>
      <p>Our approach to strata management is bound by honesty and a strong set of moral principles. We act in our clients’ best interests with diligence and transparency for understanding and accountability.</p>
    </article>
    <article class="principle">
      <h3><svg viewBox="0 0 40 36"><path d="M3 3v30h32" fill="none" stroke="var(--red)" stroke-width="2"/><rect x="7" y="22" width="5" height="10" fill="var(--red)"/><rect x="14" y="16" width="5" height="16" fill="var(--red)"/><rect x="21" y="19" width="5" height="13" fill="var(--red)"/><rect x="28" y="11" width="5" height="21" fill="var(--red)"/><path d="M7 17l8-7 6 4 11-10" fill="none" stroke="var(--red)" stroke-width="2"/></svg>Continuous Improvement</h3>
      <p>Our goal is to continually evolve to better our offering and to be adaptable and responsive to change. Our infrastructure supports us to continually mould into the business that is right for our clients.</p>
    </article>
    <article class="principle">
      <h3><svg viewBox="0 0 40 36"><rect x="4" y="3" width="22" height="30" fill="none" stroke="var(--red)" stroke-width="2.2"/><path d="M8 10h14M8 15h14M8 20h10M8 25h8" stroke="var(--red)" stroke-width="2"/><path d="M22 28l14-14 3 3-14 14-4 1z" fill="var(--red)"/></svg>Ethical Stance</h3>
      <p>We aim to create a community of ethical business relationships where we contribute our values and services to give our clients outstanding reassurance of our abilities.</p>
    </article>
  </section>
</div>
</body>
</html>
```